Cybersecurity Start-Up - Tervalo

We need a power-point design for a new company based in Madrid (Spain) called 'Tervalo'. We aim to provide cybersecurity services to small- medium size companies for whom security is critical but paying big money to huge companies is not affordable.

The final design should communicate several things. As technology company which provides cybersecurity, it should be seen as something modern and futuristic , combined with safety and protection.

The company name Tervalo comes from Tervalosa, an ancient Celtiberian settlement in Spain which is famous for its role in the Celtiberian Wars (130 BC). They fought with Rome for 20 years , while being numerical inferior. And they won several times. When a final siege ocurred after a massive deployment of Rome legions, they held their ground for more than a year without food. When the situation was not longer sustainable, they decided to commit suicide rather than become slaves.

So the vision to hold the ground no matter what, should be communicated too
Updates

Need extra days to review

Requirements
Must have
• Check files attached for the logo of the company

```html
<!DOCTYPE html>
<html lang="en">
<head>
<meta charset="utf-8">
<title>Tervalo — Presentation Template Overview</title>
<link href="https://fonts.googleapis.com/css2?family=Montserrat:wght@400;500;600;700&display=swap" rel="stylesheet">
<style>
:root{
  --navy:#1b2a3a;
  --navy-deep:#15212e;
  --navy-soft:#2a3a4c;
  --navy-row:#223142;
  --orange:#ef5b35;
  --orange-soft:#f7924a;
  --grey:#9aa3ad;
  --grey-band:#4f5d6d;
  --light:#f2f3f5;
  --ink:#2a3542;
  --muted:#8b939c;
  --white:#ffffff;
}
*{box-sizing:border-box;margin:0;padding:0}
html,body{width:1200px;height:2400px;overflow:hidden;background:var(--white)}
body{font-family:"Montserrat",Arial,sans-serif;color:var(--ink)}
.canvas{position:relative;width:1200px;height:2400px;overflow:hidden;background:var(--white)}

.slide{position:absolute;width:514px;height:290px;overflow:hidden;background:var(--white);box-shadow:0 2px 6px rgba(0,0,0,.18)}
.slide.dark{background:var(--navy);color:var(--white)}
.col-a{left:43px}.col-b{left:643px}
.row-1{top:5px}.row-2{top:304px}.row-3{top:603px}.row-4{top:902px}
.row-5{top:1202px}.row-6{top:1501px}.row-7{top:1800px}.row-8{top:2099px}

.abs{position:absolute}
.wordmark{position:absolute;font-weight:600;letter-spacing:-.5px;line-height:1;white-space:nowrap}
.wordmark.on-dark{color:var(--white)}
.wordmark.on-light{color:var(--navy)}

.slide-head{position:absolute;top:8px;left:0;height:22px;display:flex;align-items:center;padding-left:12px;font-size:15px;font-weight:600;color:var(--ink)}
.slide-head::before{content:"";position:absolute;left:0;top:0;width:6px;height:100%;background:var(--orange)}
.dark .slide-head{color:var(--white)}
.foot-logo{position:absolute;left:10px;bottom:9px;font-size:12px;font-weight:600;letter-spacing:-.3px;color:var(--navy)}
.dark .foot-logo,.foot-logo.on-dark{color:var(--white)}
.page-dot{position:absolute;right:10px;bottom:10px;width:12px;height:12px;border-radius:50%;background:var(--orange);color:var(--white);font-size:5.5px;display:flex;align-items:center;justify-content:center;font-weight:600}

.photo{position:absolute}

/* cover 1 */
.band-grey{position:absolute;height:38px;top:112px;background:var(--grey-band)}
.cover-title{position:absolute;font-weight:500;color:var(--orange);font-size:22px}

/* cover 2 & 5 */
.orange-flag{position:absolute;background:var(--orange);color:var(--white);font-size:15px;font-weight:500;line-height:1.35;display:flex;flex-direction:column;justify-content:center;text-align:center}

/* cover 3/4 */
.hero-title{position:absolute;left:24px;top:170px;font-size:24px;font-weight:600}
.hero-sub{position:absolute;left:24px;top:202px;font-size:8px;font-weight:600}

/* agenda */
.agenda-panel{position:absolute;left:0;top:0;width:176px;height:290px;background:var(--navy)}
.agenda-item{position:absolute;left:210px;width:290px;height:50px}
.diamond{position:absolute;left:0;top:4px;width:26px;height:26px;background:var(--orange);transform:rotate(45deg);box-shadow:0 0 0 3px #fde3da}
.diamond-num{position:absolute;left:0;top:4px;width:26px;height:26px;color:var(--white);font-size:13px;font-weight:600;display:flex;align-items:center;justify-content:center}
.agenda-title{position:absolute;left:58px;top:0;font-size:9.5px;font-weight:700;color:var(--orange)}
.agenda-year{position:absolute;left:58px;top:12px;font-size:5.5px;color:var(--orange)}
.agenda-text{position:absolute;left:58px;top:19px;width:140px;font-size:5.5px;line-height:1.35;color:var(--muted)}

/* malware */
.learn-more{position:absolute;left:213px;top:242px;width:72px;height:13px;border-radius:7px;background:var(--navy-deep);border:1px solid #3a4a5c;color:var(--white);font-size:5.5px;font-weight:600;display:flex;align-items:center;justify-content:center}

/* key features */
.feature{position:absolute;top:96px;width:64px;text-align:center}
.feature-icon{width:30px;height:30px;border-radius:50%;margin:0 auto 6px;display:flex;align-items:center;justify-content:center}
.feature-name{font-size:8px;font-weight:600}
.feature-text{font-size:5.5px;line-height:1.3;color:#c3cad2;margin-top:2px}
.feature-para{position:absolute;left:21px;top:182px;width:205px;font-size:6.5px;line-height:1.45;color:#d5dbe1}
.feature-para strong{color:var(--white)}

/* team */
.team{position:absolute;left:37px;top:64px;display:flex;gap:13px}
.member{width:99px}
.member .photo{position:static;width:99px;height:66px;background:linear-gradient(180deg,#e4e6e9,#c9ced4)}
.member-name{font-size:7px;font-weight:700;margin-top:6px}
.member-role{font-size:5px;color:var(--muted);margin-top:2px}
.skill{margin-top:4px}
.skill-label{font-size:4.5px;font-weight:600;color:var(--ink)}
.skill-track{height:5px;background:#d6d9dd;margin-top:1px;position:relative}
.skill-fill{position:absolute;left:0;top:0;height:5px;font-size:4px;color:var(--white);text-align:right;padding-right:2px;line-height:5px}
.fill-navy{background:var(--navy)}
.fill-orange{background:var(--orange)}
.fill-soft{background:var(--orange-soft)}
.page-num{position:absolute;left:250px;bottom:6px;font-size:7px;color:var(--ink)}

/* project design */
.pd-item{position:absolute;width:100px;font-size:5.5px;line-height:1.3;color:var(--muted)}
.pd-item b{display:block;font-size:7px;color:var(--ink);font-weight:600}
.pd-item.left{text-align:right}
.pd-item.left b{color:var(--ink)}
.pd-item .accent{color:var(--orange)}
.pd-icon{position:absolute;width:24px;height:24px;border-radius:50%;display:flex;align-items:center;justify-content:center}
.pd-note{position:absolute;left:14px;top:228px;width:486px;font-size:5.6px;line-height:1.45;color:var(--muted)}

/* chain */
.chain-desc{position:absolute;width:66px;text-align:center;font-size:4.8px;line-height:1.3;color:var(--muted)}
.chain-desc b{display:block;font-size:6px;font-weight:600;color:var(--ink)}
.chain-desc b.accent{color:var(--orange)}
.slide-no{position:absolute;right:14px;top:12px;font-size:7px;color:var(--ink)}

/* table */
.plans{position:absolute;left:32px;top:62px;width:458px;border-collapse:collapse;table-layout:fixed;font-size:6px;text-align:center}
.plans th{height:22px;color:var(--white);font-weight:600;font-size:6px;letter-spacing:.3px}
.plans th.blank{background:transparent}
.plans th.basic{background:var(--orange-soft)}
.plans th.plan{background:var(--orange)}
.plans td{height:21px;color:var(--white)}
.plans tr:nth-child(odd) td{background:var(--navy-soft)}
.plans tr:nth-child(even) td{background:var(--navy-row)}
.plans td.label{background:#36465a !important;color:#c9d0d8;font-size:5.5px}
.tick{display:inline-block;width:10px;height:10px;border-radius:50%;background:var(--orange-soft);vertical-align:middle}
.plan-btn{position:absolute;top:243px;width:54px;height:13px;border:1px solid var(--orange);border-radius:2px;color:var(--white);font-size:5.5px;font-weight:600;display:flex;align-items:center;justify-content:center}

/* thank you */
.thanks-big{position:absolute;font-size:30px;font-weight:600;color:var(--white)}
.contact{position:absolute;left:30px;display:flex;align-items:center;gap:7px;font-size:7px;color:var(--white)}
.contact svg{flex:none}
.band-orange{position:absolute;top:117px;height:36px;background:var(--orange)}
</style>
</head>
<body>
<div class="canvas">

  <!-- 1 Cover: centred wordmark on band -->
  <section class="slide dark col-a row-1">
    <div class="band-grey" style="left:0;width:109px"></div>
    <div class="band-grey" style="left:261px;width:253px"></div>
    <div class="wordmark on-dark" style="left:120px;top:117px;font-size:30px">Tervalo</div>
    <div class="cover-title" style="left:114px;top:166px">Your Title Goes Here</div>
  </section>

  <!-- 2 Cover: orange flag over network photo -->
  <section class="slide dark col-b row-1">
    <div class="photo" role="img" aria-label="Photo of a hand touching a glowing network of connected points" style="inset:0;background:radial-gradient(ellipse at 70% 40%,#3a4b5e 0%,#1f2e3f 55%,#15212e 100%)"></div>
    <div class="orange-flag" style="left:0;top:94px;width:245px;height:101px;clip-path:polygon(0 0,100% 0,86% 100%,0 100%);padding-right:30px">
      <span>Your Title Goes Here</span><span>Your Second Line Here</span>
    </div>
    <div class="wordmark on-dark" style="left:285px;top:130px;font-size:32px">Tervalo</div>
  </section>

  <!-- 3 Cover: dark code photo -->
  <section class="slide dark col-a row-2">
    <div class="photo" role="img" aria-label="Photo of green code on a dark screen with a padlock" style="inset:0;background:linear-gradient(120deg,#1a2c38 0%,#1e3a42 45%,#3a2430 70%,#15212e 100%)"></div>
    <div class="wordmark on-dark" style="left:24px;top:132px;font-size:20px">Tervalo</div>
    <div class="hero-title" style="color:var(--white)">Your Title Goes Here</div>
    <div class="hero-sub" style="color:var(--white)">Your Subtitle Goes Here</div>
  </section>

  <!-- 4 Cover: light photo -->
  <section class="slide col-b row-2">
    <div class="photo" role="img" aria-label="Faded photo of a person working at a desk" style="inset:0;background:linear-gradient(120deg,#f5f6f7 0%,#e3e5e8 55%,#d2d5d9 100%)"></div>
    <div class="wordmark on-light" style="left:24px;top:132px;font-size:20px">Tervalo</div>
    <div class="hero-title" style="color:var(--navy)">Your Title Goes Here</div>
    <div class="hero-sub" style="color:var(--navy)">Your Subtitle Goes Here</div>
  </section>

  <!-- 5 Cover: white with orange flag -->
  <section class="slide col-a row-3">
    <div class="orange-flag" style="left:0;top:90px;width:357px;height:75px;clip-path:polygon(0 0,100% 0,90% 100%,0 100%);padding-right:34px;font-size:17px">
      <span>Your Title Goes Here</span><span>Your Second Line Here</span>
    </div>
    <div class="abs" style="left:0;top:168px;width:165px;height:18px;background:#a7adb4;clip-path:polygon(0 0,100% 0,92% 100%,0 100%);color:var(--white);font-size:7.5px;font-weight:600;display:flex;align-items:center;padding-left:18px">www.yourwebsite.com</div>
    <div class="wordmark on-light" style="left:372px;top:112px;font-size:26px">Tervalo</div>
  </section>

  <!-- 6 Agenda -->
  <section class="slide col-b row-3">
    <div class="agenda-panel"></div>
    <div class="slide-head" style="color:var(--white)">Our Agenda</div>
    <div class="agenda-item" style="top:44px"><div class="diamond"></div><div class="diamond-num">1</div><div class="agenda-title">Agenda One</div><div class="agenda-year">1010</div><div class="agenda-text">Short line of agenda text goes here for the first topic in brief.</div></div>
    <div class="agenda-item" style="top:100px"><div class="diamond"></div><div class="diamond-num">2</div><div class="agenda-title">Agenda Two</div><div class="agenda-year">1020</div><div class="agenda-text">Short line of agenda text goes here for the second topic in brief.</div></div>
    <div class="agenda-item" style="top:156px"><div class="diamond"></div><div class="diamond-num">3</div><div class="agenda-title">Agenda Three</div><div class="agenda-year">1030</div><div class="agenda-text">Short line of agenda text goes here for the third topic in brief.</div></div>
    <div class="agenda-item" style="top:212px"><div class="diamond"></div><div class="diamond-num">4</div><div class="agenda-title">Agenda Four</div><div class="agenda-year">1040</div><div class="agenda-text">Short line of agenda text goes here for the fourth topic in brief.</div></div>
    <div class="foot-logo on-dark">Tervalo</div>
    <div class="page-dot">6</div>
  </section>

  <!-- 7 Malware Protection -->
  <section class="slide dark col-a row-4">
    <div class="slide-head">Malware Protection</div>
    <div class="photo" role="img" aria-label="Illustration of devices, cloud, code window, magnifier, shield and padlock with bugs" style="left:109px;top:56px;width:272px;height:150px;border-radius:6px;background:linear-gradient(180deg,#2b3b4d 0%,#e6e8eb 55%,#cfd3d8 100%)"></div>
    <div class="learn-more">LEARN MORE</div>
    <div class="foot-logo">Tervalo</div>
    <div class="page-dot">7</div>
  </section>

  <!-- 8 Key Features -->
  <section class="slide dark col-b row-4">
    <svg class="abs" style="left:0;top:0" width="514" height="290" aria-hidden="true">
      <polygon points="268,0 514,0 514,290 360,290" fill="#22344a"/>
      <polygon points="400,290 514,180 514,290" fill="#ffffff"/>
    </svg>
    <div class="slide-head">Key Features</div>
    <div class="feature" style="left:13px"><div class="feature-icon" style="background:#3b4b5e">
      <svg width="14" height="12" aria-hidden="true"><rect x="1" y="1" width="12" height="8" fill="none" stroke="#fff" stroke-width="1.2"/><line x1="4" y1="11" x2="10" y2="11" stroke="#fff" stroke-width="1.2"/></svg></div>
      <div class="feature-name">Applicable</div><div class="feature-text">Site your text here for better result.</div></div>
    <div class="feature" style="left:90px"><div class="feature-icon" style="background:var(--orange)">
      <svg width="14" height="14" aria-hidden="true"><line x1="2" y1="12" x2="12" y2="2" stroke="#fff" stroke-width="1.6"/><line x1="2" y1="2" x2="12" y2="12" stroke="#fff" stroke-width="1.6"/></svg></div>
      <div class="feature-name">Editable</div><div class="feature-text">Site your text here for better result.</div></div>
    <div class="feature" style="left:166px"><div class="feature-icon" style="background:#8c939b">
      <svg width="14" height="14" aria-hidden="true"><rect x="2" y="2" width="10" height="10" fill="none" stroke="#fff" stroke-width="1.2" stroke-dasharray="3 2"/></svg></div>
      <div class="feature-name">Free Service</div><div class="feature-text">Site your text here for better result.</div></div>
    <div class="feature-para">The <strong>Presentation Template</strong> is exclusively made and created to exceed our customer needs with tons and lots of features and benefits.</div>
    <div class="photo" role="img" aria-label="Laptop showing a photo of a modern building facade" style="left:234px;top:62px;width:280px;height:183px;border-radius:4px 0 0 4px;background:linear-gradient(135deg,#e9ecef 0%,#9aa3ad 50%,#2f3b48 100%)"></div>
    <div class="foot-logo">Tervalo</div>
    <div class="page-dot">8</div>
  </section>

  <!-- 9 Meet The Team -->
  <section class="slide col-a row-5">
    <div class="slide-head">Meet The Team</div>
    <div class="team">
      <div class="member"><div class="photo" role="img" aria-label="Portrait photo of team member Nella"></div>
        <div class="member-name">Nella</div><div class="member-role">Creative Director</div>
        <div class="skill"><div class="skill-label">HTML5</div><div class="skill-track"><div class="skill-fill fill-navy" style="width:65%">65%</div></div></div>
        <div class="skill"><div class="skill-label">PHP</div><div class="skill-track"><div class="skill-fill fill-orange" style="width:80%">80%</div></div></div>
        <div class="skill"><div class="skill-label">MySQL</div><div class="skill-track"><div class="skill-fill fill-soft" style="width:60%">60%</div></div></div></div>
      <div class="member"><div class="photo" role="img" aria-label="Portrait photo of team member David"></div>
        <div class="member-name">David</div><div class="member-role">Creative Director</div>
        <div class="skill"><div class="skill-label">HTML5</div><div class="skill-track"><div class="skill-fill fill-navy" style="width:80%">80%</div></div></div>
        <div class="skill"><div class="skill-label">PHP</div><div class="skill-track"><div class="skill-fill fill-orange" style="width:60%">60%</div></div></div>
        <div class="skill"><div class="skill-label">MySQL</div><div class="skill-track"><div class="skill-fill fill-soft" style="width:70%">70%</div></div></div></div>
      <div class="member"><div class="photo" role="img" aria-label="Portrait photo of team member Ella"></div>
        <div class="member-name">Ella</div><div class="member-role">Creative Director</div>
        <div class="skill"><div class="skill-label">HTML5</div><div class="skill-track"><div class="skill-fill fill-navy" style="width:90%">90%</div></div></div>
        <div class="skill"><div class="skill-label">PHP</div><div class="skill-track"><div class="skill-fill fill-orange" style="width:70%">70%</div></div></div>
        <div class="skill"><div class="skill-label">MySQL</div><div class="skill-track"><div class="skill-fill fill-soft" style="width:40%">40%</div></div></div></div>
      <div class="member"><div class="photo" role="img" aria-label="Portrait photo of team member Tommy"></div>
        <div class="member-name">Tommy</div><div class="member-role">Creative Director</div>
        <div class="skill"><div class="skill-label">HTML5</div><div class="skill-track"><div class="skill-fill fill-navy" style="width:60%">60%</div></div></div>
        <div class="skill"><div class="skill-label">PHP</div><div class="skill-track"><div class="skill-fill fill-orange" style="width:90%">90%</div></div></div>
        <div class="skill"><div class="skill-label">MySQL</div><div class="skill-track"><div class="skill-fill fill-soft" style="width:70%">70%</div></div></div></div>
    </div>
    <div class="page-num">9</div>
    <div class="foot-logo">Tervalo</div>
    <div class="page-dot">9</div>
  </section>

  <!-- 10 Project Design -->
  <section class="slide col-b row-5">
    <div class="slide-head">Project Design</div>
    <svg class="abs" style="left:145px;top:46px" width="220" height="120" aria-hidden="true">
      <polygon points="110,64 216,84 110,104 4,84" fill="#1b2a3a"/>
      <polygon points="110,56 216,76 110,96 4,76" fill="#3a4652"/>
      <polygon points="110,48 216,68 110,88 4,68" fill="#5e6872"/>
      <polygon points="110,40 216,60 110,80 4,60" fill="#8d949b"/>
      <polygon points="110,32 216,52 110,72 4,52" fill="#ef5b35"/>
      <polygon points="110,24 216,44 110,64 4,44" fill="#f08462"/>
      <polygon points="110,16 216,36 110,56 4,36" fill="#f2a88f"/>
      <polygon points="110,8 216,28 110,48 4,28" fill="#d9cdc8"/>
      <polygon points="110,0 216,20 110,40 4,20" fill="#eae4e1"/>
    </svg>
    <div class="pd-item left" style="left:20px;top:92px"><b>Digital</b>Nullam au tempor purus. Nunc a leo magna.</div>
    <div class="pd-icon" style="left:121px;top:95px;background:var(--navy)"><svg width="12" height="10" aria-hidden="true"><rect x="1" y="1" width="10" height="6" fill="none" stroke="#fff" stroke-width="1.2"/><line x1="4" y1="9" x2="8" y2="9" stroke="#fff" stroke-width="1.2"/></svg></div>
    <div class="pd-item left" style="left:20px;top:148px"><b class="accent">Warning</b>Nullam au tempor purus. Nunc a leo magna.</div>
    <div class="pd-icon" style="left:121px;top:150px;background:var(--orange)"><svg width="12" height="12" aria-hidden="true"><polygon points="6,1 11,11 1,11" fill="none" stroke="#fff" stroke-width="1.2"/></svg></div>
    <div class="pd-icon" style="left:364px;top:95px;background:var(--orange)"><svg width="12" height="10" aria-hidden="true"><rect x="1" y="1" width="10" height="6" rx="2" fill="#fff"/></svg></div>
    <div class="pd-item" style="left:396px;top:92px"><b class="accent">Teamwork</b>Nullam au tempor purus. Nunc a leo magna.</div>
    <div class="pd-icon" style="left:364px;top:150px;background:var(--navy)"><svg width="12" height="12" aria-hidden="true"><polygon points="6,1 10,11 2,11" fill="#fff"/></svg></div>
    <div class="pd-item" style="left:396px;top:148px"><b>Rotation</b>Nullam au tempor purus. Nunc a leo magna.</div>
    <div class="pd-note">Sample text for this slide sits here in a short line. Add a brief summary of the project design and its key stages so the audience can follow the plan, the team roles and the steps from start to the final result.</div>
    <div class="foot-logo">Tervalo</div>
    <div class="page-dot">10</div>
  </section>

  <!-- 11 Chainlink Process -->
  <section class="slide col-a row-6">
    <div class="slide-head">Chainlink Process</div>
    <div class="slide-no">11</div>
    <svg class="abs" style="left:0;top:0" width="514" height="290" aria-hidden="true">
      <g stroke-width="0">
        <circle cx="80" cy="160" r="22" fill="#1b2a3a"/>
        <circle cx="132" cy="140" r="22" fill="#ef5b35"/>
        <circle cx="184" cy="160" r="22" fill="#f7924a"/>
        <circle cx="236" cy="140" r="22" fill="#9aa3ad"/>
        <circle cx="288" cy="160" r="22" fill="#1b2a3a"/>
        <circle cx="340" cy="140" r="22" fill="#ef5b35"/>
        <circle cx="392" cy="160" r="22" fill="#f7924a"/>
        <circle cx="444" cy="140" r="22" fill="#9aa3ad"/>
      </g>
      <g fill="#ffffff">
        <circle cx="80" cy="160" r="13"/><circle cx="132" cy="140" r="13"/><circle cx="184" cy="160" r="13"/><circle cx="236" cy="140" r="13"/>
        <circle cx="288" cy="160" r="13"/><circle cx="340" cy="140" r="13"/><circle cx="392" cy="160" r="13"/><circle cx="444" cy="140" r="13"/>
      </g>
      <g fill="none" stroke-width="1.4" stroke-linecap="round">
        <polyline points="76,156 84,160 76,164" stroke="#1b2a3a"/>
        <polyline points="128,142 132,137 136,142" stroke="#ef5b35"/>
        <rect x="179" y="155" width="10" height="10" stroke="#f7924a"/>
        <polyline points="232,139 235,143 241,136" stroke="#9aa3ad"/>
        <circle cx="288" cy="160" r="5" stroke="#1b2a3a"/>
        <line x1="336" y1="144" x2="344" y2="136" stroke="#ef5b35"/><line x1="336" y1="136" x2="344" y2="144" stroke="#ef5b35"/>
        <circle cx="392" cy="158" r="4" stroke="#f7924a"/><line x1="392" y1="162" x2="392" y2="166" stroke="#f7924a"/>
        <polyline points="440,144 444,136 448,144" stroke="#9aa3ad"/>
      </g>
    </svg>
    <div class="chain-desc" style="left:99px;top:70px"><b class="accent">Description</b>Suitable for all categories business and personal presentation</div>
    <div class="chain-desc" style="left:203px;top:70px"><b>Description</b>Suitable for all categories business and personal presentation</div>
    <div class="chain-desc" style="left:307px;top:70px"><b>Description</b>Suitable for all categories business and personal presentation</div>
    <div class="chain-desc" style="left:411px;top:70px"><b>Description</b>Suitable for all categories business and personal presentation</div>
    <div class="chain-desc" style="left:47px;top:190px"><b>Description</b>Suitable for all categories business and personal presentation</div>
    <div class="chain-desc" style="left:151px;top:190px"><b class="accent">Description</b>Suitable for all categories business and personal presentation</div>
    <div class="chain-desc" style="left:255px;top:190px"><b class="accent">Description</b>Suitable for all categories business and personal presentation</div>
    <div class="chain-desc" style="left:359px;top:190px"><b class="accent">Description</b>Suitable for all categories business and personal presentation</div>
    <div class="foot-logo">Tervalo</div>
    <div class="page-dot">11</div>
  </section>

  <!-- 12 Simple Table -->
  <section class="slide dark col-b row-6">
    <div class="slide-head">Simple Table</div>
    <table class="plans">
      <colgroup><col style="width:88px"><col><col><col><col></colgroup>
      <thead><tr><th class="blank"></th><th class="basic">BASIC</th><th class="plan">STUDENT</th><th class="plan">BUSINESS</th><th class="plan">CORPORATE</th></tr></thead>
      <tbody>
        <tr><td class="label">Users</td><td>1</td><td>5</td><td>15</td><td>50</td></tr>
        <tr><td class="label">Domain Name</td><td>1</td><td>3</td><td>5</td><td>10</td></tr>
        <tr><td class="label">Storage</td><td>1 GB</td><td>5 GB</td><td>10 GB</td><td>unlimited</td></tr>
        <tr><td class="label">Uploads</td><td>10 GB</td><td>50 GB</td><td>250 GB</td><td>unlimited</td></tr>
        <tr><td class="label">Support</td><td></td><td><span class="tick"></span></td><td><span class="tick"></span></td><td><span class="tick"></span></td></tr>
        <tr><td class="label">Offer</td><td>---</td><td>---</td><td>one month free</td><td>three month free</td></tr>
      </tbody>
    </table>
    <div class="plan-btn" style="left:138px">Get this Plan</div>
    <div class="plan-btn" style="left:230px">Get this Plan</div>
    <div class="plan-btn" style="left:322px">Get this Plan</div>
    <div class="plan-btn" style="left:414px">Get this Plan</div>
    <div class="foot-logo">Tervalo</div>
    <div class="page-dot">12</div>
  </section>

  <!-- 13 Light content -->
  <section class="slide col-a row-7">
    <div class="slide-head">Your Light Content Slide</div>
    <div class="foot-logo">Tervalo</div>
    <div class="page-dot">13</div>
  </section>

  <!-- 14 Dark content -->
  <section class="slide dark col-b row-7">
    <div class="slide-head">Your Dark Content Slide</div>
    <div class="foot-logo">Tervalo</div>
    <div class="page-dot">14</div>
  </section>

  <!-- 15 Thank You with contact -->
  <section class="slide dark col-a row-8">
    <div class="photo" role="img" aria-label="Photo of a tablet and a cup of coffee on a white desk" style="inset:0;clip-path:polygon(58% 0,100% 0,100% 100%,40% 100%);background:linear-gradient(135deg,#d9dde2 0%,#f2f3f4 50%,#b8bec5 100%)"></div>
    <div class="wordmark on-dark" style="left:29px;top:30px;font-size:20px">Tervalo</div>
    <div class="thanks-big" style="left:30px;top:112px">Thank You</div>
    <div class="abs" style="left:30px;top:149px;font-size:13px;font-weight:500">Send Your Feedback</div>
    <div class="contact" style="top:180px"><svg width="8" height="10" aria-hidden="true"><path d="M4 10 L1 5 A3 3 0 1 1 7 5 Z" fill="#fff"/></svg><span>123 Street Road<br>City 12345</span></div>
    <div class="contact" style="top:204px"><svg width="8" height="8" aria-hidden="true"><path d="M1 1 L3 1 L4 3 L3 4 Q4 6 5 5 L6 4 L8 5 L8 7 Q4 8 1 1 Z" fill="#fff"/></svg><span>(123) 456-7890</span></div>
    <div class="contact" style="top:218px"><svg width="9" height="7" aria-hidden="true"><rect x="0.5" y="0.5" width="8" height="6" fill="#fff"/><polyline points="0.5,0.5 4.5,4 8.5,0.5" fill="none" stroke="#1b2a3a" stroke-width="1"/></svg><span>emailaddress@email.com</span></div>
    <div class="contact" style="top:232px"><svg width="8" height="8" aria-hidden="true"><circle cx="4" cy="4" r="3.5" fill="#fff"/></svg><span>www.website-address.com</span></div>
  </section>

  <!-- 16 Thank You closing -->
  <section class="slide dark col-b row-8">
    <div class="band-orange" style="left:0;width:133px;clip-path:polygon(0 0,100% 0,88% 100%,0 100%)"></div>
    <div class="band-orange" style="left:253px;width:261px;clip-path:polygon(6% 0,100% 0,100% 100%,0 100%)"></div>
    <div class="wordmark on-dark" style="left:150px;top:120px;font-size:30px">Tervalo</div>
    <div class="thanks-big" style="left:0;width:514px;text-align:center;top:164px">Thank You</div>
  </section>

</div>
</body>
</html>
```